Tr construction holdings pty ltd

2 sided card black and red with white
Very professional and elegant

Target Market(s)

Construction and Development

Industry/Entity Type

Construction and development

Contact Information for Business Card

One side black, one side red/or white business logo in top corner, email: morgan@trbuildworks.example

Requirements
Should not have
• Blue

```html
<!DOCTYPE html>
<html lang="en">
<head>
<meta charset="utf-8">
<title>TR Construction – Business Card</title>
<link rel="stylesheet" href="https://fonts.googleapis.com/css2?family=Lato:wght@400;700;900&display=swap">
<style>
  :root {
    --bg: #2a2a2c;
    --card-dark: #1d1d1f;
    --brand-red: #ea3a1f;
    --white: #ffffff;
    --rule: #8a8a8a;
  }
  * { margin: 0; padding: 0; box-sizing: border-box; }
  html, body { width: 1200px; height: 1108px; overflow: hidden; }
  body {
    background: var(--bg);
    font-family: 'Lato', sans-serif;
    display: flex;
    align-items: center;
    justify-content: center;
    gap: 70px;
  }
  .card {
    width: 400px;
    height: 680px;
    border-radius: 28px;
    position: relative;
    overflow: hidden;
  }
  .card-front {
    background: var(--card-dark);
    color: var(--white);
    display: flex;
    flex-direction: column;
    align-items: center;
    text-align: center;
  }
  .brand-name {
    margin-top: 140px;
    font-weight: 900;
    font-size: 30px;
    line-height: 36px;
    letter-spacing: 2px;
    text-transform: uppercase;
    white-space: nowrap;
    color: var(--white);
    display: flex;
    align-items: baseline;
    gap: 6px;
  }
  .brand-dot {
    width: 8px; height: 8px;
    background: var(--brand-red);
    flex: none;
  }
  .holder-name {
    margin-top: 110px;
    font-weight: 900;
    font-size: 30px;
    line-height: 36px;
    letter-spacing: 1px;
    color: var(--brand-red);
    text-transform: uppercase;
  }
  .holder-title {
    margin-top: 4px;
    font-size: 21px;
    line-height: 26px;
    color: var(--white);
  }
  .icon-row {
    margin-top: 16px;
    width: 290px;
    display: flex;
    align-items: center;
    gap: 8px;
  }
  .icon-row .rule { flex: 1; height: 1px; background: var(--rule); }
  .icon-box {
    width: 30px; height: 30px;
    background: var(--brand-red);
    border-radius: 4px;
    display: flex; align-items: center; justify-content: center;
  }
  .contact-list {
    margin-top: 14px;
    list-style: none;
    font-size: 20px;
    line-height: 30px;
  }
  .contact-list .accent { color: var(--brand-red); }
  .divider {
    margin-top: 12px;
    width: 300px; height: 1px; background: var(--rule);
  }
  .address {
    margin-top: 14px;
    font-size: 20px;
    line-height: 29px;
    font-style: normal;
  }
  .card-back { background: var(--brand-red); }
  .back-pattern {
    position: absolute; inset: 0;
    background: linear-gradient(160deg, #ee4226 0%, var(--brand-red) 55%, #e2351b 100%);
  }
  .back-brand {
    position: absolute;
    right: 46px;
    bottom: 210px;
    font-weight: 900;
    font-size: 26px;
    letter-spacing: 2px;
    text-transform: uppercase;
    white-space: nowrap;
    color: var(--white);
  }
</style>
</head>
<body>
  <section class="card card-front">
    <div class="brand-name">TR Construction<span class="brand-dot"></span></div>

    <h1 class="holder-name">Daniel Reeve</h1>
    <p class="holder-title">Managing Director</p>

    <div class="icon-row">
      <span class="rule"></span>
      <span class="icon-box" aria-label="Phone">
        <svg width="18" height="18" viewBox="0 0 24 24"><path fill="#fff" d="M6.6 10.8a15.1 15.1 0 0 0 6.6 6.6l2.2-2.2c.3-.3.7-.4 1-.2 1.1.4 2.3.6 3.6.6.6 0 1 .4 1 1V20c0 .6-.4 1-1 1A17 17 0 0 1 3 4c0-.6.4-1 1-1h3.5c.6 0 1 .4 1 1 0 1.3.2 2.5.6 3.6.1.3 0 .7-.2 1z"/></svg>
      </span>
      <span class="icon-box" aria-label="Email">
        <svg width="18" height="18" viewBox="0 0 24 24"><rect x="3" y="5" width="18" height="14" fill="none" stroke="#fff" stroke-width="2"/><path d="M3 5l9 8 9-8M3 19l7-7M21 19l-7-7" fill="none" stroke="#fff" stroke-width="1.6"/></svg>
      </span>
      <span class="icon-box" aria-label="Website">
        <svg width="18" height="18" viewBox="0 0 24 24"><circle cx="12" cy="12" r="9" fill="none" stroke="#fff" stroke-width="2"/><ellipse cx="12" cy="12" rx="4" ry="9" fill="none" stroke="#fff" stroke-width="1.5"/><path d="M3 12h18" stroke="#fff" stroke-width="1.5"/></svg>
      </span>
      <span class="rule"></span>
    </div>

    <ul class="contact-list">
      <li>044-555 010 220</li>
      <li>morgan@trbuildworks.example</li>
      <li>www.<span class="accent">trbuildworks</span>.example</li>
    </ul>

    <div class="divider"></div>

    <address class="address">88, Harbour Road<br>40210, Westmere</address>
  </section>

  <section class="card card-back">
    <div class="back-pattern" role="img" aria-label="Faint embossed repeating brand pattern on red"></div>
    <div class="back-brand">TR Construction</div>
  </section>
</body>
</html>
```